Velocity Pulse sharing solutions, we offer different types of mobile charging stations for all ty

I need an app that shows all the locations that use our charging stations.
the app should show the following:

1. a map where client can see where all the stations are
2. a map that shows which one is the nearest charging station based on the persons location
3. a search tab where you can pick the city ( all will be based from sweden) and we will start with two cities: Gothenburg and Stockholm. So user will be able to pick the city and than get a list of all venues using our stations. along the way we will keep adding cities and countries but for now i need a design, something i can show potential customers on a power point how this app will work.
4. a list of different venue categories:
- restaurant
- café
- Festival
- Airport
- Library
- Night club
- Shopping center

Once client chooses the city, they can also choose what they are looking for and choose for example which restaurant to eat at based on if they have our charging station or not

you can of course improvise on ideas, if you come up with something and want to add to the app design thats ok, I'm up for suggestions.

in conclusion: the purpose for the app is for users to be able to search for charging stations or see where the nearest charging station is

Target Market(s)

Everyone

Requirements
Must have
• professional and simple design

```html
<!DOCTYPE html>
<html lang="en">
<head>
<meta charset="utf-8">
<title>Velocity Pulse – Search</title>
<link href="https://fonts.googleapis.com/css2?family=Quicksand:wght@700&family=Source+Sans+3:wght@400;600&display=swap" rel="stylesheet">
<style>
  :root {
    --bg: #2e3450;
    --white: #ffffff;
    --green: #39b34a;
    --brand-green: #3cdc14;
    --blue: #0071bc;
  }
  * { margin: 0; padding: 0; box-sizing: border-box; }
  html, body { width: 675px; height: 1200px; overflow: hidden; background: var(--bg); }
  .screen {
    position: relative;
    width: 675px;
    height: 1200px;
    background: var(--bg);
    color: var(--white);
    font-family: "Source Sans 3", "Helvetica Neue", Arial, sans-serif;
  }
  .status-bar {
    position: absolute; top: 0; left: 0; right: 0; height: 36px;
    display: flex; align-items: center; justify-content: space-between;
    padding: 0 12px; font-size: 18px; font-weight: 600;
  }
  .status-bar .carrier { display: flex; align-items: center; gap: 6px; }
  .status-bar .signal { display: flex; gap: 2px; }
  .status-bar .signal i { width: 8px; height: 8px; border-radius: 50%; background: var(--white); display: block; }
  .status-bar .time { position: absolute; left: 0; right: 0; text-align: center; pointer-events: none; }
  .status-bar .battery { display: flex; align-items: center; gap: 5px; }
  .battery-icon { width: 34px; height: 15px; border: 1.5px solid var(--white); border-radius: 3px; padding: 1.5px; position: relative; }
  .battery-icon::before { content: ""; display: block; width: 100%; height: 100%; background: var(--white); border-radius: 1px; }
  .battery-icon::after { content: ""; position: absolute; right: -4px; top: 4px; width: 2px; height: 5px; background: var(--white); border-radius: 0 1px 1px 0; }

  .brand-mark {
    position: absolute; left: 272px; top: 165px;
    width: 130px; height: 130px; border-radius: 50%;
    background: var(--brand-green);
  }
  .brand-name {
    position: absolute; left: 0; right: 0; top: 325px;
    text-align: center;
    font-family: "Quicksand", "Nunito", sans-serif; font-weight: 700;
    font-size: 56px; line-height: 1; color: var(--white);
    letter-spacing: -0.5px;
  }
  .brand-tagline {
    position: absolute; left: 0; right: 0; top: 398px;
    text-align: center;
    font-family: "Quicksand", "Nunito", sans-serif; font-weight: 700;
    font-size: 18px; letter-spacing: 0.5em; padding-left: 0.5em;
  }

  .search-label {
    position: absolute; left: 0; right: 0; top: 555px;
    text-align: center; font-size: 25px;
  }
  .option-icons { position: absolute; left: 0; top: 0; width: 675px; height: 1200px; }
  .option-label {
    position: absolute; top: 872px; width: 260px;
    text-align: center; font-size: 27px; line-height: 33px;
    text-transform: uppercase;
  }
  .option-label.station { left: 45px; }
  .option-label.venue { left: 377px; }

  .button {
    position: absolute; left: 81px; width: 513px; height: 63px;
    border-radius: 32px; border: none;
    display: flex; align-items: center; justify-content: center;
    color: var(--white); font-family: inherit; font-size: 27px;
  }
  .button-search { top: 1009px; background: var(--blue); }
  .button-city { top: 1088px; background: var(--green); }
  .button-city .back-arrow { position: absolute; left: 112px; top: 22px; }
</style>
</head>
<body>
<main class="screen">
  <header class="status-bar">
    <div class="carrier">
      <span class="signal"><i></i><i></i><i></i><i></i><i></i></span>
      <span>Nordtel</span>
      <svg width="20" height="15" viewBox="0 0 20 15" aria-hidden="true">
        <path d="M10 14 L7 10.5 A4.5 4.5 0 0 1 13 10.5 Z" fill="#fff"/>
        <path d="M4.5 8 A8 8 0 0 1 15.5 8" stroke="#fff" stroke-width="2.2" fill="none"/>
        <path d="M1.5 5 A12 12 0 0 1 18.5 5" stroke="#fff" stroke-width="2.2" fill="none"/>
      </svg>
    </div>
    <div class="time">9:41 AM</div>
    <div class="battery"><span>100%</span><span class="battery-icon"></span></div>
  </header>

  <div class="brand-mark" aria-hidden="true"></div>
  <h1 class="brand-name">Velocity Pulse</h1>
  <p class="brand-tagline">Charging solutions</p>

  <p class="search-label">SEARCH BY :</p>

  <svg class="option-icons" viewBox="0 0 750 1334" aria-hidden="true">
    <!-- station option (selected) -->
    <circle cx="200" cy="840" r="122" fill="none" stroke="var(--green)" stroke-width="6"/>
    <circle cx="200" cy="840" r="110" fill="var(--white)"/>
    <path d="M228 768 L147 857 L200 857 L170 917 L250 826 L203 826 Z" fill="var(--green)"/>
    <!-- venue option -->
    <circle cx="553" cy="840" r="110" fill="var(--white)"/>
    <g fill="var(--green)">
      <path d="M512 794 L549 768 L586 794 Z"/>
      <rect x="497" y="798" width="105" height="5"/>
      <rect x="493" y="895" width="110" height="7"/>
      <rect x="603" y="815" width="10" height="33" rx="5"/>
    </g>
    <g>
      <rect x="500" y="803" width="97" height="92" fill="var(--green)"/>
      <g fill="var(--white)">
        <rect x="514" y="813" width="11" height="13"/><rect x="533" y="813" width="11" height="13"/>
        <rect x="552" y="813" width="11" height="13"/><rect x="571" y="813" width="11" height="13"/>
        <rect x="514" y="840" width="11" height="13"/><rect x="533" y="840" width="11" height="13"/>
        <rect x="552" y="840" width="11" height="13"/><rect x="571" y="840" width="11" height="13"/>
        <rect x="514" y="867" width="11" height="13"/><rect x="571" y="867" width="11" height="13"/>
        <path d="M537 895 V874 A11 11 0 0 1 559 874 V895 Z"/>
      </g>
    </g>
  </svg>
  <p class="option-label station">Our near<br>station to you</p>
  <p class="option-label venue">Near venue<br>to you</p>

  <button class="button button-search">Search</button>
  <button class="button button-city">
    <svg class="back-arrow" width="20" height="20" viewBox="0 0 20 20" aria-hidden="true"><path d="M1 10 L19 1 V19 Z" fill="#fff"/></svg>
    Change City
  </button>
</main>
</body>
</html>
```